" Um grupo de investidores brasileiros e portugueses foi formado para lançar um condomínio em Portugal, nos arredores de Lisboa. A construtora, Zeva! Módulos, é especializada em casas feitas com containers. Vejam nosso instagram @rimo.brisal para conhecer mais sobre o nosso mercado. Apesar das casas serem container, neste projeto elas serão revestidas externamente, será um condomínio de luxo, porém com estilo mais moderno. "

```html
<!DOCTYPE html>
<html lang="pt">
<head>
<meta charset="utf-8">
<title>Alvorada – Papel Timbrado</title>
<link rel="stylesheet" href="https://fonts.googleapis.com/css2?family=Quicksand:wght@400;600&display=swap">
<style>
  :root {
    --backdrop: #e6e8e7;
    --paper: #ffffff;
    --brand-green: #5b8c2f;
    --deep-green: #3e7a28;
    --accent-orange: #cf7a2b;
    --watermark: #f0f1f0;
    --ink: #4a4f4a;
  }
  * { margin: 0; padding: 0; box-sizing: border-box; }
  html, body {
    width: 1200px; height: 1200px; overflow: hidden;
    background: var(--backdrop);
    font-family: "Quicksand", sans-serif;
  }
  .letterhead {
    position: absolute; left: 212px; top: 51px;
    width: 776px; height: 1098px;
    background: var(--paper);
    overflow: hidden;
    box-shadow: 0 6px 24px rgba(0,0,0,0.08);
  }
  .watermark {
    position: absolute; left: 230px; top: 290px;
    width: 660px; height: 660px; border-radius: 50%;
    background: var(--watermark);
  }
  .brand {
    position: absolute; left: 44px; top: 40px;
    display: flex; align-items: center; gap: 12px;
  }
  .brand-dot {
    width: 62px; height: 62px; border-radius: 50%;
    background: var(--brand-green);
  }
  .brand-text { display: flex; flex-direction: column; }
  .brand-name {
    font-weight: 600; font-size: 40px; line-height: 1;
    letter-spacing: 3px; color: var(--brand-green);
  }
  .brand-tagline {
    font-weight: 600; font-size: 11px; letter-spacing: 2.2px;
    color: var(--brand-green); margin-top: 4px;
  }
  .rule-top {
    position: absolute; left: 250px; right: 38px; top: 118px;
    height: 5px; background: var(--accent-orange);
  }
  .contact {
    position: absolute; left: 44px; top: 900px;
    list-style: none; display: flex; flex-direction: column; gap: 12px;
  }
  .contact li {
    display: flex; align-items: center; gap: 8px;
    font-size: 11px; color: var(--ink);
  }
  .contact svg { width: 16px; height: 16px; flex: none; }
  .rule-bottom {
    position: absolute; left: 44px; right: 38px; top: 1002px;
    height: 5px; background: var(--deep-green);
  }
</style>
</head>
<body>
  <main class="letterhead">
    <div class="watermark" role="img" aria-label="Marca da Alvorada em grande formato, esmaecida"></div>

    <header class="brand">
      <span class="brand-dot"></span>
      <div class="brand-text">
        <span class="brand-name">ALVORADA</span>
        <span class="brand-tagline">DAS OLIVEIRAS</span>
      </div>
    </header>
    <div class="rule-top"></div>

    <ul class="contact">
      <li>
        <svg viewBox="0 0 16 16"><circle cx="8" cy="8" r="8" fill="var(--brand-green)"/><path d="M5.5 4.5l1.5 0 .7 1.8-1 .7a5 5 0 0 0 2.3 2.3l.7-1 1.8.7v1.5c0 .5-.5 1-1 1A6.5 6.5 0 0 1 4.5 5.5c0-.5.5-1 1-1z" fill="#fff"/></svg>
        +351 210 000 000
      </li>
      <li>
        <svg viewBox="0 0 16 16"><circle cx="8" cy="8" r="8" fill="var(--brand-green)"/><path d="M8 3.5a3 3 0 0 1 3 3c0 2.2-3 6-3 6s-3-3.8-3-6a3 3 0 0 1 3-3z" fill="#fff"/><circle cx="8" cy="6.5" r="1.1" fill="var(--brand-green)"/></svg>
        Rua das Oliveiras, 12, Lisboa
      </li>
      <li>
        <svg viewBox="0 0 16 16"><circle cx="8" cy="8" r="8" fill="var(--brand-green)"/><rect x="4" y="5" width="8" height="6" rx="0.8" fill="#fff"/><path d="M4.3 5.4L8 8.3l3.7-2.9" fill="none" stroke="var(--brand-green)" stroke-width="0.9"/></svg>
        ola@alvorada.pt
      </li>
    </ul>
    <div class="rule-bottom"></div>
  </main>
</body>
</html>
```